New: Beef Jerky Labels
*per supplied logo and JPEG's
I want my logo incorporated into the batch of needed labels for my beef jerky products.
Type: Modern, Masculine, Professional
Food
I need a GENERIC label done which can then be changed via color schemes for each label of different flavors of beef jerky. I have supplied various JPEG's of another companies labels for spacing and general overview of what is on the label's. The main part that needs disgned for mine will be the above area of the lablels as all of the nutironal information, the KSB label, the ingredients and the UPC (blank white box) will stay the same. The onyl thing different at the bottom would be my company information which is to be submitted in its place. Product of Copper Falls Trail - Pine Hollow, Riverton 45021 - www.tedkorvane.com
I do NOT want the same look and I am looking for something different and more eye catching to the public for sales. I have also supplied my company logo for use in all labels. The only other needed things on label would be the actual Flavor - Made in USA - 100% Quality Beef
The sizes needed are 5" x 1" - 3" x 3" - 5.75" x 4" and they are listed as follows:
5.75" x 4" Mild, Spicy, Honey & Jalapeno Flavors (50 Count PKG's)
3" x 3" Deli Style Mild & Spicy (8oz. Delli PKG's)
3" x 3" and 5" x 1" for Mild, Spicy, Honey, Jalapeno, Teriyaki & Beef / Cheese (Sticks)
5.75" x 4" Mild, Spicy, Jalapeno & Beef / Cheese (7oz. Beef Sticks)
5.75" x 4" Mild, Spicy, Black Pepper & Jalapeno (3.25oz PKG's)
5.75" x 4" Mild, Spicy, Black Pepper & Jalapeno (15oz. PKG's)
Thanks in advance for your hard work.

```html
<!DOCTYPE html>
<html lang="en">
<head>
<meta charset="utf-8">
<title>Copper Falls Trail Beef Jerky Labels</title>
<link rel="stylesheet" href="https://fonts.googleapis.com/css2?family=Oswald:wght@500;700&family=Permanent+Marker&family=Roboto+Condensed:wght@400;700&display=swap">
<style>
  :root{
    --canvas:#ffffff;
    --kraft:#bfae8c;
    --kraft-line:#a8966f;
    --ink:#141414;
    --paper:#ffffff;
    --honey:#e8c21a;
    --spicy:#d3242a;
    --mild:#3c9a34;
    --orange:#f0a21c;
    --teriyaki:#2aa6dc;
  }
  *{box-sizing:border-box;margin:0;padding:0}
  html,body{width:1200px;height:1035px;overflow:hidden;background:var(--canvas)}
  body{position:relative;font-family:"Roboto Condensed",sans-serif;color:var(--ink)}

  .label{position:absolute;overflow:hidden;border:2px solid var(--ink);
    background:repeating-linear-gradient(90deg,var(--kraft) 0 5px,var(--kraft-line) 5px 6px);}
  .label > *{position:absolute}

  .header-band{left:0;right:0;background:var(--ink)}
  .brand{left:0;right:0;text-align:center;color:var(--paper);font-family:"Oswald",sans-serif;font-weight:700;letter-spacing:1px;line-height:1}
  .badge{border-radius:50%;display:flex;align-items:center;justify-content:center;text-align:center;
    color:var(--paper);font-family:"Oswald",sans-serif;font-weight:700;line-height:1.05;transform:rotate(-12deg)}
  .quality{color:var(--paper);font-family:"Oswald",sans-serif;font-weight:700;text-align:center;line-height:1.1}
  .flavor{left:0;right:0;text-align:center;font-family:"Permanent Marker",cursive;line-height:1;white-space:nowrap}
  .product{left:0;right:0;text-align:center;font-family:"Oswald",sans-serif;font-weight:700;color:var(--ink);line-height:1;letter-spacing:1px;white-space:nowrap}
  .info-band{left:0;right:0;background:var(--ink);color:var(--paper);text-align:center;font-weight:700;letter-spacing:.5px;display:flex;align-items:center;justify-content:center}
  .panel{background:var(--paper);border:1px solid var(--ink)}
  .nutrition{padding:4px;font-size:9px;line-height:1.2}
  .nutrition strong{display:block;font-size:13px;border-bottom:3px solid var(--ink);margin-bottom:3px}
  .cert{background:var(--paper);border:2px solid var(--ink);border-radius:50%}
  .fine{font-size:9px;line-height:1.25;color:var(--ink)}
  .count{font-size:10px;font-weight:700;white-space:nowrap}

  /* large 5.75 x 4 */
  .label--large{width:375px;height:580px;top:15px}
  .label--large .header-band{top:28px;height:222px}
  .label--large .brand{top:150px;font-size:44px}
  .label--large .badge{left:14px;top:20px;width:82px;height:82px;font-size:12px}
  .label--large .quality{right:16px;top:42px;font-size:15px}
  .label--large .flavor{top:260px;font-size:28px}
  .label--large .product{top:298px;font-size:70px}
  .label--large .info-band{top:388px;height:26px;font-size:12px}
  .label--large .nutrition{left:16px;top:428px;width:130px;height:86px}
  .label--large .cert{left:160px;top:430px;width:44px;height:44px}
  .label--large .fine.ingredients{left:160px;top:482px;width:200px}
  .label--large .upc{right:16px;top:428px;width:140px;height:46px}
  .label--large .fine.maker{left:16px;top:524px;width:240px}
  .label--large .count{right:16px;top:540px}

  /* square 3 x 3 */
  .label--square{width:280px;height:330px;top:615px}
  .label--square .header-band{top:22px;height:118px}
  .label--square .brand{top:84px;font-size:26px;white-space:nowrap}
  .label--square .badge{left:10px;top:16px;width:56px;height:56px;font-size:9px}
  .label--square .quality{right:10px;top:28px;font-size:11px}
  .label--square .flavor{top:148px;font-size:20px}
  .label--square .product{top:176px;font-size:48px}
  .label--square .info-band{top:240px;height:20px;font-size:9px}
  .label--square .fine.ingredients{left:12px;top:272px;width:150px}
  .label--square .cert{left:168px;top:270px;width:30px;height:30px}
  .label--square .upc{right:10px;top:268px;width:60px;height:40px}
  .label--square .count{left:12px;top:306px;font-size:9px}

  /* strip 5 x 1 */
  .label--strip{left:265px;top:960px;width:670px;height:66px}
  .label--strip .header-band{left:0;top:0;bottom:0;width:150px;right:auto}
  .label--strip .brand{left:0;right:auto;width:150px;top:24px;font-size:15px;white-space:nowrap}
  .label--strip .flavor{left:160px;right:auto;top:4px;width:190px;font-size:14px}
  .label--strip .product{left:160px;right:auto;top:22px;width:190px;font-size:34px}
  .label--strip .fine.maker{left:362px;top:8px;width:190px}
  .label--strip .cert{left:362px;top:38px;width:20px;height:20px}
  .label--strip .upc{right:10px;top:8px;width:90px;height:36px}
  .label--strip .count{right:10px;top:48px;font-size:9px}

  .honey-jal{--accent:var(--honey)}
  .spicy{--accent:var(--spicy)}
  .mild{--accent:var(--mild)}
  .honey{--accent:var(--orange)}
  .teriyaki{--accent:var(--teriyaki)}
  .label .badge{background:var(--accent)}
  .label .flavor{color:var(--accent)}
</style>
</head>
<body>

<section class="label label--large honey-jal" style="left:15px">
  <div class="header-band"></div>
  <div class="badge">DELICIOUS<br>FLAVOUR</div>
  <div class="quality">100%<br>QUALITY<br>BEEF</div>
  <div class="brand">COPPER FALLS TRAIL</div>
  <div class="flavor">HONEY &amp; JALAPENO</div>
  <div class="product">BEEF JERKY</div>
  <div class="info-band">MADE IN USA • REFRIGERATE AFTER OPENING</div>
  <div class="panel nutrition"><strong>Nutrition Facts</strong>Serving 28g · Calories 80</div>
  <div class="cert" role="img" aria-label="Inspection badge"></div>
  <div class="fine ingredients">Ingredients: beef, water, salt, spices, sugar.</div>
  <div class="panel upc"></div>
  <div class="fine maker">Product of Copper Falls Trail - Pine Hollow, Riverton 45021 - www.tedkorvane.com</div>
  <div class="count">10 Count PKG</div>
</section>

<section class="label label--large spicy" style="left:412px">
  <div class="header-band"></div>
  <div class="badge">DELICIOUS<br>FLAVOUR</div>
  <div class="quality">100%<br>QUALITY<br>BEEF</div>
  <div class="brand">COPPER FALLS TRAIL</div>
  <div class="flavor">SPICY</div>
  <div class="product">BEEF JERKY</div>
  <div class="info-band">MADE IN USA • REFRIGERATE AFTER OPENING</div>
  <div class="panel nutrition"><strong>Nutrition Facts</strong>Serving 28g · Calories 80</div>
  <div class="cert" role="img" aria-label="Inspection badge"></div>
  <div class="fine ingredients">Ingredients: beef, water, salt, spices, sugar.</div>
  <div class="panel upc"></div>
  <div class="fine maker">Product of Copper Falls Trail - Pine Hollow, Riverton 45021 - www.tedkorvane.com</div>
  <div class="count">10 Count PKG</div>
</section>

<section class="label label--large mild" style="left:810px">
  <div class="header-band"></div>
  <div class="badge">DELICIOUS<br>FLAVOUR</div>
  <div class="quality">100%<br>QUALITY<br>BEEF</div>
  <div class="brand">COPPER FALLS TRAIL</div>
  <div class="flavor">MILD</div>
  <div class="product">BEEF JERKY</div>
  <div class="info-band">MADE IN USA • REFRIGERATE AFTER OPENING</div>
  <div class="panel nutrition"><strong>Nutrition Facts</strong>Serving 28g · Calories 80</div>
  <div class="cert" role="img" aria-label="Inspection badge"></div>
  <div class="fine ingredients">Ingredients: beef, water, salt, spices, sugar.</div>
  <div class="panel upc"></div>
  <div class="fine maker">Product of Copper Falls Trail - Pine Hollow, Riverton 45021 - www.tedkorvane.com</div>
  <div class="count">10 Count PKG</div>
</section>

<section class="label label--square spicy" style="left:15px">
  <div class="header-band"></div>
  <div class="badge">DELICIOUS<br>FLAVOUR</div>
  <div class="quality">100%<br>QUALITY<br>BEEF</div>
  <div class="brand">COPPER FALLS TRAIL</div>
  <div class="flavor">SPICY</div>
  <div class="product">BEEF JERKY</div>
  <div class="info-band">MADE IN USA • 100% QUALITY BEEF</div>
  <div class="fine ingredients">Keep refrigerated after opening</div>
  <div class="cert" role="img" aria-label="Inspection badge"></div>
  <div class="panel upc"></div>
  <div class="count">Net Wt 3 oz</div>
</section>

<section class="label label--square mild" style="left:313px">
  <div class="header-band"></div>
  <div class="badge">DELICIOUS<br>FLAVOUR</div>
  <div class="quality">100%<br>QUALITY<br>BEEF</div>
  <div class="brand">COPPER FALLS TRAIL</div>
  <div class="flavor">MILD</div>
  <div class="product">BEEF JERKY</div>
  <div class="info-band">MADE IN USA • 100% QUALITY BEEF</div>
  <div class="fine ingredients">Keep refrigerated after opening</div>
  <div class="cert" role="img" aria-label="Inspection badge"></div>
  <div class="panel upc"></div>
  <div class="count">Net Wt 3 oz</div>
</section>

<section class="label label--square honey" style="left:610px">
  <div class="header-band"></div>
  <div class="badge">DELICIOUS<br>FLAVOUR</div>
  <div class="quality">100%<br>QUALITY<br>BEEF</div>
  <div class="brand">COPPER FALLS TRAIL</div>
  <div class="flavor">HONEY</div>
  <div class="product">BEEF JERKY</div>
  <div class="info-band">MADE IN USA • 100% QUALITY BEEF</div>
  <div class="fine ingredients">Keep refrigerated after opening</div>
  <div class="cert" role="img" aria-label="Inspection badge"></div>
  <div class="panel upc"></div>
  <div class="count">Net Wt 3 oz</div>
</section>

<section class="label label--square teriyaki" style="left:907px">
  <div class="header-band"></div>
  <div class="badge">DELICIOUS<br>FLAVOUR</div>
  <div class="quality">100%<br>QUALITY<br>BEEF</div>
  <div class="brand">COPPER FALLS TRAIL</div>
  <div class="flavor">TERIYAKI</div>
  <div class="product">BEEF JERKY</div>
  <div class="info-band">MADE IN USA • 100% QUALITY BEEF</div>
  <div class="fine ingredients">Keep refrigerated after opening</div>
  <div class="cert" role="img" aria-label="Inspection badge"></div>
  <div class="panel upc"></div>
  <div class="count">Net Wt 3 oz</div>
</section>

<section class="label label--strip mild">
  <div class="header-band"></div>
  <div class="brand">COPPER FALLS TRAIL</div>
  <div class="flavor">MILD</div>
  <div class="product">BEEF JERKY</div>
  <div class="fine maker">Product of Copper Falls Trail - Pine Hollow, Riverton 45021 - www.tedkorvane.com</div>
  <div class="cert" role="img" aria-label="Inspection badge"></div>
  <div class="panel upc"></div>
  <div class="count">Net Wt 1 oz</div>
</section>

</body>
</html>
```